KOVER Wealth Partners Brochure
Brochure Design 2011
Your Objectives Through Independence
We need a tri-fold brochure for our company KOVER Wealth Partners. We already have a custom logo created and need that inserted into the brochure. We are a independent financial services company, we offer investment advice and products to consumers and business.
Financial Services
Consumers & Business
Must use our current company logo,you can get it here:
https://photoshelf-example.net/MarcusLindt/KOVERWealthPartners?authkey=Xq7TmLbNZr2Wd9YkHfPe&feat=directlink
Also need all content including sections to be editable. Need at least three sections (Example: "The Company", "Our Services", etc...)
KOVER Wealth Partners Logo
Logo AI file
Logo AI File 2.0
Old Brochure Cover (Prime Ledger)
old brochure Inner (Prime Ledger)
This is a brochure which I like the style, simple and clean
Another Brochure in which I like
by far my favorite one, hope this inspires some ideas
more ideas

```html
<!DOCTYPE html>
<html lang="en">
<head>
<meta charset="utf-8">
<title>KOVER Wealth Partners Brochure</title>
<link href="https://fonts.googleapis.com/css2?family=PT+Sans:wght@400;700&display=swap" rel="stylesheet">
<style>
:root{
  --bg:#ecebe7;
  --paper:#ffffff;
  --green:#8aa62a;
  --green-dark:#5f7a14;
  --ink:#3d3d3d;
  --muted:#8a8a8a;
  --line:#cfcfcf;
  --photo-a:#c9c2b3;
  --photo-b:#9ea7ad;
}
*{margin:0;padding:0;box-sizing:border-box}
html,body{width:1200px;height:468px;overflow:hidden;background:var(--bg)}
body{font-family:"PT Sans",Arial,sans-serif;color:var(--ink);position:relative}
.sheet{position:absolute;top:78px;width:480px;height:312px;background:var(--paper);display:flex;box-shadow:0 2px 6px rgba(0,0,0,.18)}
.sheet--outer{left:108px}
.sheet--inner{left:612px}
.panel{width:160px;height:100%;position:relative;padding:12px 10px}
.panel+.panel{border-left:1px solid #eee}
.photo{background:linear-gradient(135deg,var(--photo-a),var(--photo-b))}
.tagline{color:var(--green);font-size:9.5px;font-weight:700;text-transform:uppercase;line-height:1.25;letter-spacing:.3px;margin-top:14px}
.tagline-rule{height:1px;background:var(--green);margin:6px 0 0;width:110px}
.intro{position:absolute;left:10px;right:8px;top:120px;display:flex;gap:6px}
.intro .photo{width:42px;height:34px;flex:none}
.intro p{font-size:5.5px;color:var(--green-dark);line-height:1.35}
.back-note{font-size:4.5px;color:var(--muted);text-align:center;line-height:1.4;margin-top:2px}
.mark{position:absolute;top:104px;left:0;right:0;text-align:center}
.mark .square{display:inline-block;width:10px;height:10px;background:var(--green);vertical-align:middle;margin-right:4px}
.mark .name{font-size:18px;font-weight:700;color:var(--green-dark);vertical-align:middle;letter-spacing:1px}
.address{position:absolute;top:150px;left:0;right:0;font-size:4.5px;color:var(--muted);text-align:center;line-height:1.5}
.cover-rule{position:absolute;left:6px;top:48px;width:1px;height:80px;background:var(--green)}
.cover-title{position:absolute;left:16px;top:52px;color:var(--green);font-size:13px;font-weight:700;line-height:1.2;text-transform:uppercase}
.badge{position:absolute;right:10px;bottom:10px;width:18px;height:12px;background:var(--green)}
.box{border:1px solid var(--line);border-radius:5px;padding:5px 6px;margin-bottom:6px}
.box h2{font-size:7px;color:var(--green-dark);text-transform:uppercase;letter-spacing:.4px;margin-bottom:3px;display:flex;align-items:center;gap:3px}
.box h2 .dot{width:4px;height:4px;border-radius:50%;background:var(--green)}
.box h3{font-size:6px;color:var(--green-dark);margin-bottom:3px;display:flex;align-items:center;gap:3px}
.box h3 .dot{width:4px;height:4px;border-radius:50%;background:var(--green)}
.box p,.box li{font-size:4.5px;line-height:1.4;color:var(--ink)}
.box ul{list-style:none}
.box li::before{content:"› ";color:var(--green)}
.row{display:flex;gap:5px;align-items:flex-start}
.row .photo{width:30px;height:24px;flex:none;border-radius:2px}
.company{height:118px}
.company .photo{width:100%;height:40px;margin-top:4px;border-radius:2px}
.service{height:96px}
</style>
</head>
<body>
<section class="sheet sheet--outer" aria-label="Brochure outside">
  <div class="panel">
    <h1 class="tagline">Flexible solutions for<br>your business needs</h1>
    <div class="tagline-rule"></div>
    <div class="intro">
      <div class="photo" role="img" aria-label="Photo of a business meeting"></div>
      <p>KOVER's simple approach to financial services brings business clarity, tailored to its timeline and goals.</p>
    </div>
  </div>
  <div class="panel">
    <p class="back-note">Independent advice for consumers and business</p>
    <div class="mark"><span class="square"></span><span class="name">KOVER</span></div>
    <p class="address">KOVER Wealth Partners<br>214 Harbor Lane, Suite 5<br>Portview, NC 28401<br>(555) 014-2286</p>
  </div>
  <div class="panel">
    <div class="cover-rule"></div>
    <h2 class="cover-title">Your<br>objectives<br>through<br>independence</h2>
    <div class="badge"></div>
  </div>
</section>

<section class="sheet sheet--inner" aria-label="Brochure inside">
  <div class="panel">
    <div class="box company">
      <h2>The Company</h2>
      <p>KOVER Wealth Partners is an independent financial services firm offering investment advice and products to consumers and business owners alike.</p>
      <div class="photo" role="img" aria-label="Photo of an office team"></div>
    </div>
    <div class="box service">
      <h2><span class="dot"></span>Our Investment Solutions</h2>
      <ul>
        <li>Retirement income planning</li>
        <li>Managed portfolio accounts</li>
        <li>Education savings plans</li>
        <li>Estate and legacy planning</li>
        <li>Business succession plans</li>
      </ul>
    </div>
  </div>
  <div class="panel">
    <div class="box service" style="height:68px">
      <h3><span class="dot"></span>Free Consulting</h3>
      <div class="row"><p>Meet with an advisor to review your goals at no cost.</p><div class="photo" role="img" aria-label="Photo of an advisor with client"></div></div>
    </div>
    <div class="box service" style="height:108px">
      <h3><span class="dot"></span>Financial Planning</h3>
      <div class="row"><div class="photo" role="img" aria-label="Photo of planning documents"></div><p>A clear plan built around your income, savings and future needs.</p></div>
    </div>
    <div class="box service" style="height:100px">
      <h3><span class="dot"></span>Tax Planning</h3>
      <div class="row"><p>Strategies that help you keep more of what you earn each year.</p><div class="photo" role="img" aria-label="Photo of a calculator and forms"></div></div>
    </div>
  </div>
  <div class="panel">
    <div class="box service" style="height:88px">
      <h3><span class="dot"></span>Real Estate</h3>
      <div class="row"><div class="photo" role="img" aria-label="Photo of a house"></div><p>Guidance on property as part of a balanced portfolio.</p></div>
    </div>
    <div class="box service" style="height:96px">
      <h3><span class="dot"></span>Mortgage Lending</h3>
      <div class="row"><p>Competitive home loans matched to your budget and plans.</p><div class="photo" role="img" aria-label="Photo of house keys"></div></div>
    </div>
    <div class="box service" style="height:92px">
      <h3><span class="dot"></span>Insurance</h3>
      <div class="row"><div class="photo" role="img" aria-label="Photo of a family outdoors"></div><p>Protection for your family, assets and business.</p></div>
    </div>
  </div>
</section>
</body>
</html>
```